Brindlecove (main name) sharpening systems(underneath)

Specializing in Knife, Scissors and Clipper sharpening, repair and maintenance.
I would like a logo designed that has at least one of the elements above showing what could happen as a result of the instrument being sharpened by my company as part of the logo (maybe the word Brindlecove being cut in half)

Target Market(s)

commercial (restaurants or any establishment that deals with food preparation, salons, barbershops) residential (any homes that use knives scissors or clippers)

Contact Information for Business Card

Name: Marcus Pellingham
Address: K240 Coral Vista Heights
Cell: 12465917362
Email: brindlecovehone@mailtrove.net

Requirements
Must have
• Brindlecove....sharpening systems clean front with strong logo indicating what we do as part of logo front of card
• Contact details: back of card
• we sharpen on site or pick up and drop off within 24hrs (at back of Card)
• telephone number: (at back) for contact
• address and other details (at back)

```html
<!DOCTYPE html>
<html lang="en">
<head>
<meta charset="utf-8">
<title>Brindlecove Sharpening Systems – Business Card</title>
<link rel="stylesheet" href="https://fonts.googleapis.com/css2?family=Open+Sans:wght@400;800&family=Questrial&display=swap">
<style>
  :root {
    --backdrop: #5e3634;
    --card-dark: #231f20;
    --card-light: #ffffff;
    --ink-light: #ffffff;
    --ink-dark: #231f20;
    --accent: #f7941d;
  }
  * { margin: 0; padding: 0; box-sizing: border-box; }
  html, body {
    width: 1200px;
    height: 1200px;
    overflow: hidden;
    background: var(--backdrop);
  }
  .canvas {
    position: relative;
    width: 1200px;
    height: 1200px;
  }
  .card {
    position: absolute;
    left: 255px;
    width: 691px;
    height: 391px;
    font-family: "Open Sans", sans-serif;
    text-align: center;
  }
  .card--front { top: 183px; background: var(--card-dark); color: var(--ink-light); }
  .card--back  { top: 626px; background: var(--card-light); color: var(--ink-dark); }

  .brand {
    position: absolute;
    left: 0;
    right: 0;
    display: flex;
    justify-content: center;
  }
  .brand-lockup {
    display: flex;
    flex-direction: column;
    align-items: flex-end;
  }
  .brand-name {
    font-weight: 800;
    text-transform: uppercase;
    letter-spacing: 1px;
    line-height: 1;
  }
  .brand-tagline {
    font-family: "Questrial", sans-serif;
    text-transform: uppercase;
    line-height: 1;
  }
  .card--front .brand { top: 74px; }
  .card--front .brand-name { font-size: 60px; }
  .card--front .brand-tagline { font-size: 21px; letter-spacing: 3px; margin-top: 8px; }
  .card--back .brand { top: 84px; }
  .card--back .brand-name { font-size: 45px; }
  .card--back .brand-tagline { font-size: 16px; letter-spacing: 2.4px; margin-top: 6px; }

  .service-line {
    position: absolute;
    top: 238px;
    left: 0;
    right: 0;
    font-family: "Questrial", sans-serif;
    font-size: 19.5px;
    color: var(--accent);
  }
  .address {
    position: absolute;
    top: 311px;
    left: 0;
    right: 0;
    font-size: 17px;
  }

  .contact-name {
    position: absolute;
    top: 247px;
    left: 0;
    right: 0;
    font-size: 25px;
  }
  .divider {
    position: absolute;
    top: 289px;
    left: 158px;
    width: 375px;
    height: 2px;
    background: linear-gradient(to right, rgba(35,31,32,0), var(--ink-dark) 20%, var(--ink-dark) 80%, rgba(35,31,32,0));
  }
  .phone {
    position: absolute;
    top: 304px;
    left: 0;
    right: 0;
    font-size: 17px;
    display: flex;
    justify-content: center;
    align-items: center;
    gap: 8px;
  }
  .phone svg { width: 12px; height: 17px; }
</style>
</head>
<body>
<main class="canvas">
  <section class="card card--front">
    <div class="brand">
      <div class="brand-lockup">
        <div class="brand-name">Brindlecove</div>
        <div class="brand-tagline">Sharpening Systems</div>
      </div>
    </div>
    <p class="service-line">we sharpen on site or pick up and drop off within 24hrs</p>
    <p class="address">K240 Coral Vista Heights</p>
  </section>

  <section class="card card--back">
    <div class="brand">
      <div class="brand-lockup">
        <div class="brand-name">Brindlecove</div>
        <div class="brand-tagline">Sharpening Systems</div>
      </div>
    </div>
    <p class="contact-name">Marcus Pellingham</p>
    <div class="divider"></div>
    <p class="phone">
      <svg viewBox="0 0 12 17" aria-hidden="true">
        <rect x="1" y="1" width="10" height="15" rx="2" fill="none" stroke="#231f20" stroke-width="1.6"/>
        <rect x="3" y="3.5" width="6" height="9" fill="#231f20"/>
      </svg>
      <span>12465917362</span>
    </p>
  </section>
</main>
</body>
</html>
```